New Electrical Contractor looking for local work

I have just started working for myself as an Electrical Contractor, based in the eastern suburbs of Melbourne. I want to advertise in the local area so hopefully I can create a client base that is close to home, so I thought a flyer that I could drop in letterboxes could be a good start. Most of my experience has been domestic houses, so ideally this is the work I would like to get more of.

Here is a list of the work I usually do:
Extensions / Renovations
Safety Switch and Switchboard Upgrades
LED Lighting including downlights/light fittings and LED strip light
Re-wires
Maintenance

I have also added a couple of images of LED strip lights and how they can be used in homes. There are a lot more on google images if anyone thinks they could be of use.

These are my details:
Business name - Dermot Hale Electrical
Phone - 0438 276 512
ABN - 52 918 407 336
REC - 37815
Email - halewireworks@brightmail.test

I will attach my business logo and business card
Updates

Could I please ask for all designs to delete the "(contractors registration number)" text.

Only REC 37815 needs to be displayed.

Thank you kindly

Industry/Entity Type

Business

Requirements
Must have
• My contact details, ie. Name, Phone, email, ABN, REC etc

```html
<!DOCTYPE html>
<html lang="en">
<head>
<meta charset="utf-8">
<title>Dermot Hale Electrical – Flyer</title>
<link rel="stylesheet" href="https://fonts.googleapis.com/css2?family=Roboto+Condensed:wght@400;700&family=Open+Sans:wght@400;600&display=swap">
<style>
  :root {
    --blue-deep: #1c3f94;
    --blue-mid: #2a63b8;
    --blue-light: #6fb3e6;
    --orange: #f28c1c;
    --grey-band: #8a8d92;
    --heading-grey: #505357;
    --service-blue: #1b6fb8;
    --navy: #27307f;
    --ink: #2b2b2b;
    --paper-top: #ffffff;
    --paper-bottom: #dde8f2;
  }
  * { margin: 0; padding: 0; box-sizing: border-box; }
  html, body { width: 935px; height: 1200px; overflow: hidden; background: #ffffff; }
  .flyer {
    position: relative;
    width: 935px;
    height: 1200px;
    overflow: hidden;
    background: linear-gradient(180deg, var(--paper-top) 40%, var(--paper-bottom) 100%);
    font-family: "Roboto Condensed", sans-serif;
  }
  .header-bands { position: absolute; inset: 0; width: 935px; height: 560px; }
  .hero-art {
    position: absolute; left: 86px; top: 28px; width: 175px; height: 258px;
    border-radius: 50% 50% 30% 30%;
    background: radial-gradient(circle at 50% 40%, #ffffff 0%, #dfe6ee 45%, rgba(120,150,190,0) 75%);
  }
  .brand { position: absolute; left: 290px; top: 50px; color: #fff; }
  .brand-name {
    font-weight: 700; font-size: 88px; line-height: 84px; letter-spacing: 1px;
    text-transform: uppercase;
  }
  .brand-tagline {
    margin-top: 22px; font-size: 27px; letter-spacing: 6px; font-weight: 400;
  }
  .services { position: absolute; left: 55px; top: 440px; }
  .services-title {
    font-weight: 700; font-size: 46px; color: var(--heading-grey); margin-bottom: 16px;
  }
  .service-list { list-style: none; }
  .service-list li {
    display: flex; align-items: center; gap: 14px;
    font-weight: 700; font-size: 33px; line-height: 42px; color: var(--service-blue);
    margin-bottom: 8px;
  }
  .service-list .continued { padding-left: 66px; margin-top: -8px; }
  .pointer { width: 52px; height: 24px; flex: none; }
  .pair { margin-left: 26px; display: inline-flex; align-items: center; gap: 14px; }
  .gallery { position: absolute; left: 57px; top: 787px; display: flex; gap: 12px; }
  .gallery-tile {
    position: relative; height: 158px; border-radius: 10px;
    border: 2px solid #ffffff; box-shadow: 0 1px 4px rgba(0,0,0,.35);
  }
  .tile-room { width: 267px; background: linear-gradient(135deg, #3a2a4a, #a25a9a 55%, #e6b86a); }
  .tile-strip { width: 261px; background: linear-gradient(135deg, #1e2126, #4a4e55 50%, #c24a6a); }
  .tile-wiring { width: 264px; background: linear-gradient(135deg, #f3f1ef, #e8c9b6 55%, #c8453a); }
  .tile-caption {
    position: absolute; left: 10px; bottom: 6px; font-family: "Open Sans", sans-serif;
    font-size: 10px; color: #ffffff;
  }
  .contact { position: absolute; left: 57px; top: 990px; color: var(--navy); }
  .contact-name { font-size: 30px; font-weight: 400; }
  .contact-phone { font-size: 50px; font-weight: 700; line-height: 56px; }
  .contact-email { margin-top: 12px; font-size: 30px; color: var(--service-blue); }
  .contact-email strong { color: var(--ink); font-weight: 700; font-size: 28px; }
  .credentials {
    margin-top: 12px; font-family: "Open Sans", sans-serif; font-size: 15px;
    font-weight: 600; color: var(--ink); word-spacing: 1px;
  }
  .credentials span + span { margin-left: 22px; }
  .cable-art {
    position: absolute; left: 665px; top: 930px; width: 270px; height: 270px;
    background: linear-gradient(150deg, rgba(255,255,255,0) 10%, #c79a5a 30%, #d22a24 55%, #2a3a8a 85%);
    clip-path: polygon(30% 0, 100% 10%, 100% 100%, 15% 100%, 0 40%);
  }
</style>
</head>
<body>
<main class="flyer">
  <svg class="header-bands" viewBox="0 0 935 560" aria-hidden="true">
    <defs>
      <linearGradient id="header-fill" x1="0" y1="0" x2="1" y2="0.6">
        <stop offset="0" stop-color="#7cc0ee"/>
        <stop offset="0.35" stop-color="#2f6fc2"/>
        <stop offset="1" stop-color="#1c3f94"/>
      </linearGradient>
    </defs>
    <path d="M0,0 H935 V490 C800,440 620,365 400,356 C260,350 130,370 0,430 Z" fill="var(--orange)"/>
    <path d="M0,0 H935 V515 C820,410 620,340 390,337 C250,335 120,355 0,405 Z" fill="var(--grey-band)"/>
    <path d="M0,0 H935 V462 C800,380 600,320 380,320 C240,320 120,340 0,395 Z" fill="url(#header-fill)"/>
  </svg>

  <div class="hero-art" role="img" aria-label="Light bulb held by a hand making an OK sign"></div>

  <header class="brand">
    <h1 class="brand-name">Dermot Hale<br>Electrical</h1>
    <p class="brand-tagline">A GRADE &nbsp;ELECTRICIAN</p>
  </header>

  <section class="services">
    <h2 class="services-title">SERVICES INCLUDES</h2>
    <ul class="service-list">
      <li><svg class="pointer" viewBox="0 0 52 24"><path d="M0,6 H34 V0 L52,12 L34,24 V18 H0 Z" fill="var(--orange)"/></svg>Extensions / Renovations</li>
      <li><svg class="pointer" viewBox="0 0 52 24"><path d="M0,6 H34 V0 L52,12 L34,24 V18 H0 Z" fill="var(--orange)"/></svg>Safety Switch &amp; Switchboard Upgrades</li>
      <li><svg class="pointer" viewBox="0 0 52 24"><path d="M0,6 H34 V0 L52,12 L34,24 V18 H0 Z" fill="var(--orange)"/></svg>Re-wires
        <span class="pair"><svg class="pointer" viewBox="0 0 52 24"><path d="M0,6 H34 V0 L52,12 L34,24 V18 H0 Z" fill="var(--orange)"/></svg>Maintenance</span></li>
      <li><svg class="pointer" viewBox="0 0 52 24"><path d="M0,6 H34 V0 L52,12 L34,24 V18 H0 Z" fill="var(--orange)"/></svg>LED Lighting &nbsp;including downlights</li>
      <li class="continued">Light Fittings &nbsp;and LED Strip Light</li>
    </ul>
  </section>

  <section class="gallery">
    <div class="gallery-tile tile-room" role="img" aria-label="Living room lit with LED strip lighting"><span class="tile-caption">LED strip light</span></div>
    <div class="gallery-tile tile-strip" role="img" aria-label="Coiled LED strip light with controller board"><span class="tile-caption">LED strip light</span></div>
    <div class="gallery-tile tile-wiring" role="img" aria-label="Hands stripping electrical wires with pliers"></div>
  </section>

  <div class="cable-art" role="img" aria-label="Cut electrical cables showing copper strands"></div>

  <section class="contact">
    <p class="contact-name">CONTACT ME - DERMOT HALE</p>
    <p class="contact-phone">0438 276 512</p>
    <p class="contact-email">Email: <strong>halewireworks@brightmail.test</strong></p>
    <p class="credentials"><span>ABN - 52 918 407 336</span><span>REC - 37815</span></p>
  </section>
</main>
</body>
</html>
```